Financial Advisor needs a BOLD Business Card

I need a business card that is professional, and is also eye-catching and memorable. I would like to include my photo (several different professional photos have been uploaded). Preferred primary color is blue, or green, or dark purple. The final design should have a modern/contemporary look while communicating a professional image.

Target Market(s)

Individual Investors and Small Business Owners

Industry/Entity Type

Business

Contact Information for Business Card

[side 1:] Dale Korvanek Financial Advisor 58271 Marbleton Creek Rd., #340 St. Louis, MO 63907 (314) 555-0182 main (314) 555-0927 cell (314) 555-0346 fax daleK@qrvlx.com [side 2:] Life Insurance | Retirement | Employee Benefits

Font styles to use
Serif
Sans Serif

Requirements
Must have
• [disclaimer, text can be 7-9 point:] Securities offered through the B.W. Harbor Trading Company. Member NARCU/TLOB. Four Quarry Plaza, Cincinnati, Ohio 45917. 513-555-0263. Investment Advisory Services offered through B.W. Holdings Management Company.
Nice to have
• Bright, Light & Airy feel on Side 1 with contact data, bold patterns, high color contrast, modern or 3D look
Should not have
• Any symbols referring to money (e.g. $)

```html
<!DOCTYPE html>
<html lang="en">
<head>
<meta charset="utf-8">
<title>Dale Korvanek – Business Card</title>
<link rel="stylesheet" href="https://fonts.googleapis.com/css2?family=Lato:wght@400;700;900&display=swap">
<style>
  :root {
    --navy: #10163a;
    --gold: #d8b744;
    --paper: #eef3fa;
    --white: #ffffff;
    --muted: #b9bfd6;
    --stage: #e6e6e6;
    --ink: #14193a;
  }
  * { margin: 0; padding: 0; box-sizing: border-box; }
  html, body { width: 1200px; height: 900px; overflow: hidden; }
  body {
    background: var(--stage);
    font-family: "Lato", Arial, sans-serif;
    position: relative;
  }
  .card {
    position: absolute;
    width: 630px;
    height: 360px;
    overflow: hidden;
    box-shadow: 0 10px 30px rgba(0,0,0,0.25);
  }

  /* Front side */
  .card-front { left: 90px; top: 70px; background: var(--paper); }
  .brand {
    position: absolute; left: 40px; top: 62px;
    color: var(--navy); font-weight: 700;
    text-transform: uppercase; line-height: 1.25;
  }
  .brand-name { font-size: 22px; letter-spacing: 1px; }
  .brand-sub { font-size: 9px; letter-spacing: 2px; padding-left: 40px; }
  .portrait {
    position: absolute; left: 438px; top: 16px;
    width: 176px; height: 190px;
    background: linear-gradient(160deg, #3a3026 0%, #1f2226 55%, #2b2f36 100%);
    border: 3px solid var(--white);
  }
  .address {
    position: absolute; left: 28px; top: 216px;
    font-size: 14px; color: var(--ink);
  }
  .contact-band {
    position: absolute; left: 0; top: 240px;
    width: 420px; height: 120px;
    background: var(--navy);
    border-top: 5px solid var(--gold);
    border-top-right-radius: 60px;
  }
  .contact-list {
    position: absolute; top: 26px;
    list-style: none; color: var(--white);
    font-size: 14px;
  }
  .contact-list li { display: flex; align-items: center; gap: 12px; height: 24px; }
  .contact-list svg { width: 18px; height: 16px; fill: var(--white); }
  .contact-list.phones { left: 44px; }
  .contact-list.online { left: 236px; }
  .name-plate {
    position: absolute; left: 432px; top: 226px;
    width: 198px; height: 72px;
    background: var(--gold);
    border-top-left-radius: 10px;
    color: var(--ink); text-align: center;
    padding-top: 8px; line-height: 1.25;
  }
  .name-plate .person { font-size: 19px; font-weight: 400; }
  .name-plate .person strong { font-weight: 900; }
  .name-plate .role, .name-plate .direct { font-size: 13px; }

  /* Back side */
  .card-back { left: 480px; top: 470px; background: var(--navy); }
  .services-band {
    position: absolute; left: 270px; top: 140px;
    width: 360px; height: 62px;
    background: var(--gold);
    border-top-left-radius: 16px;
    display: flex; align-items: center; justify-content: flex-end;
    padding-right: 30px;
    color: var(--white); font-weight: 700; font-size: 13px;
    letter-spacing: 0.4px; white-space: nowrap;
  }
  .disclaimer {
    position: absolute; left: 40px; right: 40px; bottom: 22px;
    color: var(--muted); font-size: 9px; line-height: 1.45;
    text-align: center;
  }
</style>
</head>
<body>

<section class="card card-front" aria-label="Business card front">
  <div class="brand">
    <div class="brand-name">Crestline Ridge</div>
    <div class="brand-sub">Financial Group</div>
  </div>

  <div class="portrait" role="img" aria-label="Portrait photo of Dale Korvanek in a dark suit"></div>

  <p class="address">58271 Marbleton Creek Rd., #340 St. Louis, MO 63907</p>

  <div class="contact-band">
    <ul class="contact-list phones">
      <li>
        <svg viewBox="0 0 18 16" aria-hidden="true"><path d="M2 4c0-2 3-3 7-3s7 1 7 3v1h-4V4H6v1H2zM4 7h10l2 8H2z"/></svg>
        (314) 555-0927
      </li>
      <li>
        <svg viewBox="0 0 18 16" aria-hidden="true"><path d="M4 1h8l2 2v3H4zM1 7h16v6h-3v2H4v-2H1zM6 11v3h6v-3z"/></svg>
        (314) 555-0346
      </li>
    </ul>
    <ul class="contact-list online">
      <li>
        <svg viewBox="0 0 18 16" aria-hidden="true"><path d="M1 2h16v12H1zm2 2v.5l6 4 6-4V4l-6 4z" fill-rule="evenodd"/></svg>
        daleK@qrvlx.com
      </li>
      <li>
        <svg viewBox="0 0 18 16" aria-hidden="true"><path d="M1 1h16v11H11v2h2v1H5v-1h2v-2H1zm2 2v7h12V3z" fill-rule="evenodd"/></svg>
        www.crfgx.com
      </li>
    </ul>
  </div>

  <div class="name-plate">
    <div class="person">Dale <strong>Korvanek</strong></div>
    <div class="role">Financial Adviser</div>
    <div class="direct">(314) 555-0182</div>
  </div>
</section>

<section class="card card-back" aria-label="Business card back">
  <div class="services-band">Life Insurance | Retirement | EmployeeBenefits</div>
  <p class="disclaimer">Securities offered through the B.W. Harbor Trading Company. Member NARCU/TLOB. Four Quarry Plaza, Cincinnati, Ohio 45917. 513-555-0263. Investment Advisory Services offered through B.W. Holdings Management Company.</p>
</section>

</body>
</html>
```